Designers, here is a last minute change-
Please switch the two left and middle back panel, so that exclusions are on the back middle panel. If you need to remove the boxes and make the font smaller that is fine..
The bullet points underneath should be INDENTED UNDERNEATH that bullet point.
Under the benefits section, this bullet point should look like this:
"The inability of the insured to reach the venue solely and directly due to:
-Strikes, riots, civil commotion, martial law or
-Flood, fire, explosion or
-Through the act of a constituted authority to
protect public health and safety
-Adverse weather, including snow, fog, frost or storm"
Designers,
Here is the order that the content should be in for the brochure:
Inside brochure:
Left- About the policy
Middle: the Benefits & continued on the right panel
Right- continued benefits
Back of brochure:
Left- Exclusions
Middle: Who we are & Contact info
Right- The front of the brochure
Please use your judgment where you see these exclusions going on the brochure.
Exclusions
Not all circumstances leading to a cancellation are covered. The following is a list of exclusions. VERĪN does not cover any loss directly or indirectly arising out of, or contributed to by, or resulting from:
Any contractual dispute or breach
Lack of diligence the results of which would increase the risk, and/or likelihood of a loss
Failure to observe and comply with the requirements of any law, ordinance, court or regulatory body of whatever jurisdiction
Fraud, misrepresentation or concealment by the Insured
Actual or threatened war
Any financial failure of or financial default by anyone
Change in rate of exchange, rate of interest or stability of any currency
Loss of damage caused in whole or part by radioactivity
Seizure or destruction under quarantine or customs regulations
Seepage and/or pollution and/or contamination unless it is discovered during the period of insurance and is a direct cause of loss
Failure in the event of bodily injury or sickness to consult a duly qualified medical practitioner and comply with the medical advice
Death, bodily injury or sickness of the Insured directly or indirectly cause by or resulting from: suicide or intentional self injury or criminal act
Any influenza variant or communicable disease which prior to or simultaneously with the loss arising, is declared an epidemic or pandemic by the Global Health Council
Actual or threatened malicious use of pathogenic or poisonous biological or chemical materials
Any act of or threat of or fear of terrorism
Any loss arising from mourning whether declared or not
Any procedure where the venue is not within the United States
Any loss or claim in excess of the limit(s) stated in the certificate
Any loss due to the failure or inability of any computer or computer equipment (whether owned by the insured or not)
Other exclusions may apply. See your policy for details.
This brochure provides an overview of VERĪN coverage. Certain limitations and exclusions apply. Complete details are provided in your policy. In the event of any conflict between the brochure and policy interpretation, the language of the policy will apply in all cases.
Please make sure there is a space between each of the bullet points.
Your VERĪN Benefits
VERĪN is your protection should you have a loss beyond your control including:
-Incapacity requiring a hospital stay of at least 24 hours occurring in the seven (7) days immediately prior to the date of the procedure through accident, bodily injury or sickness
-Death of the Insured within the thirty (30) days of the procedure immediately prior to the date of the procedure
-Death of a family member of the Insured’s immediate family within the fourteen (14) days immediately prior to the date of the procedure
-Travel delay solely and directly due to the mechanical failure of or accidental damage to the transport in which the Insured is travelling or a cause outside of the control of the Insured that solely and directly prevents the Insured’s continued safe transit
-The unavoidable requirement of the Insured to perform jury service where the jury summons was first received by the Insured after the date of the Insured contracting for the procedure
-The inability of the insured to reach the venue solely and directly due to:
Strikes, riots, civil commotion, martial law or
Flood, fire, explosion or
Through the act of a constituted authority to protect public health and safety
Adverse weather, including snow, fog, frost or storm
-The unavoidable requirement for the Insured to remain at home due to the serious damage to the Insured’s home or place of business caused by fire, aircraft, explosion, storm, flood, subsidence, earthquake, falling trees, burst pipes, lightning, malicious persons or theft
Trifold brochure please
We would like The logo to be 'VERĪN'. There is no logo to go along with it. It can be in any font as long as it is clearly displayed. The color scheme we would like to work with is soft colors like silver, white, light blue, and light green. It should look like it fits in with a doctor's office.
Please use your own photos from PixBarrow. We have provided reference photos in the brief for the type of pictures we are looking for.
RT/KWP/HN Team
About Us:
VERĪN was developed by Harwell Shield of New Jersey, named the 40th largest insurance brokerage in the US by Risk Ledger magazine. Harwell is ranked among the top 20 privately-held property/casualty agencies in the U.S. by Broker Digest magazine, and it is among the Top 5 privately held brokerage firms in New Jersey. VERIN is underwritten by Pinecrest Mutual Insurance Company, which has received an "A" (Excellent) or higher rating from the R.T. Vole Company for over 100 years (most recent rating evaluation effective March 29, 2012).
For more information or to file a claim contact:
Scheduled Treatment Deposit Guard Plan
Harwell Shield Company of NJ
Address Line 1
Address Line 2
Direct:
Fax:
Email:
Website:
This should be the opening to the brochure- what the patients should read first:
All types of surgery, including the finances you put into them, hold some type of risk. It may take only moments to decide on a procedure, but months to decide on the right surgeon for you.
After selecting your surgeon, you must decide how to finance your procedure. Unfortunately, most health insurance policies do not provide coverage. Most cosmetic surgeons require advance payment including a non-refundable deposit. While cancellation policies vary, almost every cancellation results in losing money- even if you have a valid reason. What happens if you have to cancel due to circumstances beyond your control? Now your deposit can be protected thanks to VERIN- the scheduled treatment deposit guard plan. VERIN protects you when the unexpected happens and you have to cancel your cosmetic surgery.
VERĪN is offered to all patients of plastic surgeons who have a cancellation policy. This policy is based on each individual patient and all elective surgeries are covered, no matter how small.

```html
<!DOCTYPE html>
<html lang="en">
<head>
<meta charset="utf-8">
<title>Verin Trifold – Back</title>
<link href="https://fonts.googleapis.com/css2?family=Open+Sans:wght@400;600;700;800&family=Raleway:wght@300;400&display=swap" rel="stylesheet">
<style>
  :root{
    --sky:#5fb6e6;
    --sky-deep:#2f95d3;
    --sky-pale:#cfe8f6;
    --silver:#9aa0a5;
    --ink:#5b6166;
    --ink-soft:#7d8389;
    --white:#ffffff;
  }
  *{box-sizing:border-box;margin:0;padding:0}
  html,body{width:1200px;height:935px;overflow:hidden;background:#f2f4f5}
  .brochure{position:relative;width:1200px;height:935px;background:var(--white);overflow:hidden;font-family:"Open Sans",sans-serif;color:var(--ink)}
  .top-band{position:absolute;left:0;top:0;width:800px;height:16px;background:linear-gradient(90deg,var(--sky-pale),var(--sky) 45%,var(--sky-pale))}
  .waves{position:absolute;left:0;top:0;width:1200px;height:935px;pointer-events:none}
  .panel{position:absolute;top:0;height:935px;width:400px}
  .panel--about{left:0}
  .panel--exclusions{left:400px;border-left:1px solid #e6ecef}
  .panel--cover{left:800px;border-left:1px solid #e6ecef;background:linear-gradient(180deg,#f7fbfd,#ffffff 60%)}

  /* About */
  .about-title{position:absolute;left:40px;top:178px;font-weight:800;font-size:44px;color:var(--silver);letter-spacing:.5px}
  .about-text{position:absolute;left:40px;top:268px;width:330px;font-size:16.5px;line-height:1.42;color:var(--ink-soft)}
  .echo{position:absolute;font-family:"Open Sans",sans-serif;font-weight:600;color:rgba(255,255,255,.45);white-space:nowrap;z-index:2}

  /* Exclusions */
  .excl-title{position:absolute;left:22px;top:26px;font-weight:700;font-size:21px;color:var(--sky-deep)}
  .excl-body{position:absolute;left:22px;top:60px;width:360px;font-size:9.3px;line-height:1.24;color:var(--ink-soft)}
  .excl-body p{margin-bottom:5px}
  .excl-list{list-style:none;margin:2px 0 6px 6px}
  .excl-list li{position:relative;padding-left:10px;margin-bottom:3px}
  .excl-list li::before{content:"";position:absolute;left:0;top:4px;width:4px;height:4px;border-radius:50%;background:var(--sky)}
  .contact{position:absolute;left:0;top:662px;width:400px;text-align:center;color:var(--ink)}
  .contact-title{font-size:19px;line-height:1.25;font-weight:400;margin-bottom:14px}
  .contact-lines{font-size:12.5px;line-height:1.5;color:var(--ink-soft)}

  /* Cover */
  .photo{position:absolute;left:110px;top:40px;width:290px;height:560px;background:radial-gradient(ellipse at 55% 38%,#f1ddd0 0%,#e2c6b6 35%,#c9d9e4 70%,#e9f1f6 100%)}
  .wordmark{position:absolute;left:22px;top:58px;font-family:"Open Sans",sans-serif;font-weight:600;font-size:84px;line-height:1;color:var(--sky-deep)}
  .tagline{position:absolute;right:26px;top:528px;font-family:"Raleway",sans-serif;font-weight:400;font-size:22px;color:var(--sky-deep);text-align:right;line-height:1.2;z-index:2}
  .plan-name{position:absolute;left:18px;top:660px;width:382px;font-family:"Raleway",sans-serif;font-weight:300;font-size:33px;color:var(--sky);letter-spacing:2px;line-height:1}
  .plan-line{display:flex;align-items:center;height:44px}
  .plan-line span{white-space:nowrap}
  .plan-line i{flex:1;height:1px;background:var(--sky);margin-left:10px;position:relative}
  .plan-line i::after{content:"";position:absolute;right:14px;top:-3px;width:7px;height:7px;border-radius:50%;background:var(--sky)}
</style>
</head>
<body>
<div class="brochure">
  <div class="top-band"></div>

  <section class="panel panel--about">
    <h2 class="about-title">About Us:</h2>
    <p class="about-text">Verin was developed by Harwell Shield of New Jersey, named the 40th largest insurance brokerage in the US by Risk Ledger magazine. Harwell is ranked among the top 20 privately-held property/casualty agencies in the U.S. by Broker Digest magazine, and it is among the Top 5 privately held brokerage firms in New Jersey. Verin is underwritten by Pinecrest Mutual Insurance Company, which has received an "A" (Excellent) or higher rating from the R.T. Vole Company for over 100 years (most recent rating evaluation effective March 29, 2012).</p>
  </section>

  <section class="panel panel--exclusions">
    <h2 class="excl-title">Exclusions</h2>
    <div class="excl-body">
      <p>Not all circumstances leading to a cancellation are covered. The following is a list of exclusions. Verin does not cover any loss directly or indirectly arising out of, or contributed to by, or resulting from:</p>
      <ul class="excl-list">
        <li>Any contractual dispute or breach</li>
        <li>Lack of diligence the results of which would increase the risk, and/or likelihood of a loss</li>
        <li>Failure to observe and comply with the requirements of any law, ordinance, court or regulatory body of whatever jurisdiction</li>
        <li>Fraud, misrepresentation or concealment by the Insured</li>
        <li>Actual or threatened war</li>
        <li>Any financial failure of or financial default by anyone</li>
        <li>Change in rate of exchange, rate of interest or stability of any currency</li>
        <li>Loss of damage caused in whole or part by radioactivity</li>
        <li>Seizure or destruction under quarantine or customs regulations</li>
        <li>Seepage and/or pollution and/or contamination unless it is discovered during the period of insurance and is a direct cause of loss</li>
        <li>Failure in the event of bodily injury or sickness to consult a duly qualified medical practitioner and comply with the medical advice</li>
        <li>Death, bodily injury or sickness of the Insured directly or indirectly cause by or resulting from: suicide or intentional self injury or criminal act</li>
        <li>Any influenza variant or communicable disease which prior to or simultaneously with the loss arising, is declared an epidemic or pandemic by the Global Health Council</li>
        <li>Actual or threatened malicious use of pathogenic or poisonous biological or chemical materials</li>
        <li>Any act of or threat of or fear of terrorism</li>
        <li>Any loss arising from mourning whether declared or not</li>
        <li>Any procedure where the venue is not within the United States</li>
        <li>Any loss or claim in excess of the limit(s) stated in the certificate</li>
        <li>Any loss due to the failure or inability of any computer or computer equipment (whether owned by the insured or not)</li>
      </ul>
      <p>Other exclusions may apply. See your policy for details.</p>
      <p>This brochure provides an overview of Verin coverage. Certain limitations and exclusions apply. Complete details are provided in your policy. In the event of any conflict between the brochure and policy interpretation, the language of the policy will apply in all cases.</p>
    </div>
    <div class="contact">
      <h3 class="contact-title">For more information or<br>to file a claim contact:</h3>
      <div class="contact-lines">
        Scheduled Treatment Deposit Guard Plan<br>
        Harwell Shield Company of NJ<br>
        Address Line 1: 24 Orchard Row, Suite 3<br>
        Address Line 2: Fairhill, NJ 07000<br>
        Direct: (555) 010-4400 &nbsp; Fax: (555) 010-4401<br>
        Email: claims@verinplan.example<br>
        Website: verinplan.example
      </div>
    </div>
  </section>

  <section class="panel panel--cover">
    <div class="photo" role="img" aria-label="Photo of a calm patient with clear skin, soft light-blue backdrop"></div>
    <div class="wordmark">Verin</div>
    <div class="tagline">Escape the<br>Unexpected</div>
    <div class="plan-name">
      <div class="plan-line"><span>SCHEDULED</span><i></i></div>
      <div class="plan-line"><span>TREATMENT</span><i></i></div>
      <div class="plan-line"><span>DEPOSIT GUARD</span><i></i></div>
      <div class="plan-line"><span>PLAN</span><i></i></div>
    </div>
  </section>

  <svg class="waves" viewBox="0 0 1200 935" aria-hidden="true">
    <defs>
      <linearGradient id="waveA" x1="0" y1="0" x2="1" y2="0">
        <stop offset="0" stop-color="#2f95d3"/>
        <stop offset=".45" stop-color="#7cc4ec"/>
        <stop offset="1" stop-color="#cfe8f6"/>
      </linearGradient>
      <linearGradient id="waveB" x1="0" y1="0" x2="1" y2="0">
        <stop offset="0" stop-color="#cfe8f6"/>
        <stop offset=".5" stop-color="#9fd3f0"/>
        <stop offset="1" stop-color="#5fb6e6"/>
      </linearGradient>
    </defs>
    <path d="M0 700 C150 650 300 720 400 690 L400 935 L0 935 Z" fill="url(#waveA)" opacity=".9"/>
    <path d="M0 760 C160 720 300 800 400 760 L400 935 L0 935 Z" fill="#5fb6e6" opacity=".55"/>
    <path d="M400 905 C600 870 800 920 1200 860 L1200 935 L400 935 Z" fill="url(#waveB)" opacity=".8"/>
    <path d="M0 890 C300 860 700 935 1200 900 L1200 935 L0 935 Z" fill="#2f95d3" opacity=".7"/>
    <path d="M800 612 C930 575 1060 635 1200 598 L1200 636 C1060 672 930 612 800 650 Z" fill="#7cc4ec" opacity=".7"/>
    <path d="M800 602 C950 594 1080 600 1200 578" stroke="#ffffff" stroke-width="2" fill="none" opacity=".8"/>
  </svg>

  <div class="echo" style="left:30px;top:722px;font-size:54px">Verin</div>
  <div class="echo" style="left:160px;top:772px;font-size:42px">Verin</div>
  <div class="echo" style="left:60px;top:818px;font-size:34px">Verin</div>
</div>
</body>
</html>
```